Letterhead and business cards for criminal defense law firm
with existing logo
Letterhead and business cards for criminal defense law firm - Law
Creative Brief
Simple
The Law Office of Marcus Varek, PLLC
718 Birchwood Avenue, Suite 300 Houston, TX 77019
Varek@BrightCounselGroup.net
I would like to incorporate our slogan: Experienced criminal defense lawyers Or if you think of a better slogan/motto, feel free to incorporate it. I am not a flashy or showy lawyer. I want the card to invoke credibility, stability and intelligence (not an ambulance chaser or sleazy lawyer).

```html
<!DOCTYPE html>
<html lang="en">
<head>
<meta charset="utf-8">
<title>Marcus Varek, PLLC – Stationery</title>
<link href="https://fonts.googleapis.com/css2?family=Montserrat:wght@400;600;700&display=swap" rel="stylesheet">
<style>
  :root {
    --navy: #2b2d4f;
    --ink: #33354f;
    --grey: #8a8c98;
    --rule: #b9bbc4;
    --faint: #e6e7ea;
    --paper: #ffffff;
    --stage: #ffffff;
  }
  * { box-sizing: border-box; margin: 0; padding: 0; }
  html, body { width: 1200px; height: 936px; overflow: hidden; background: var(--stage); }
  body { font-family: "Montserrat", sans-serif; color: var(--ink); position: relative; }

  .piece { position: absolute; background: var(--paper); overflow: hidden;
           box-shadow: 0 2px 8px rgba(0,0,0,.18); }
  .piece svg.edge { position: absolute; inset: 0; width: 100%; height: 100%; }

  .brand { position: absolute; display: flex; align-items: center; gap: 8px; }
  .brand .mark { background: var(--navy); flex: none; }
  .brand .name { font-weight: 700; color: var(--navy); text-transform: uppercase; letter-spacing: .04em; white-space: nowrap; }

  /* letterhead */
  .letterhead { left: 183px; top: 63px; width: 388px; height: 551px; }
  .letterhead .brand { left: 28px; top: 26px; }
  .letterhead .brand .mark { width: 20px; height: 20px; }
  .letterhead .brand .name { font-size: 13px; }
  .letterhead .contact { position: absolute; left: 226px; top: 26px; font-size: 6px; line-height: 10px; color: var(--grey); white-space: nowrap; }
  .letterhead .ghost { position: absolute; left: 0; right: 0; top: 248px; display: flex; justify-content: center; align-items: center; gap: 10px; }
  .ghost .mark { width: 44px; height: 44px; background: var(--faint); }
  .ghost .name { font-size: 20px; font-weight: 700; color: var(--faint); text-transform: uppercase; letter-spacing: .04em; white-space: nowrap; }

  /* folder */
  .folder { left: 634px; top: 38px; width: 459px; height: 579px; }
  .folder .lockup { position: absolute; left: 0; right: 0; top: 205px; display: flex; flex-direction: column; align-items: center; }
  .folder .lockup .mark { width: 52px; height: 52px; background: var(--navy); margin-bottom: 10px; }
  .folder .lockup .office { font-size: 7px; color: var(--grey); text-transform: uppercase; letter-spacing: .1em; width: 150px; text-align: left; }
  .folder .lockup .name { font-size: 21px; font-weight: 700; color: var(--navy); text-transform: uppercase; letter-spacing: .04em; line-height: 1.2; white-space: nowrap; }
  .folder .lockup .suffix { font-size: 7px; color: var(--grey); letter-spacing: .1em; width: 150px; text-align: right; }

  /* business cards */
  .card-front { left: 43px; top: 655px; width: 180px; height: 96px; }
  .card-front .brand { left: 12px; top: 12px; gap: 5px; }
  .card-front .brand .mark { width: 10px; height: 10px; }
  .card-front .brand .name { font-size: 8px; }
  .card-front .person { position: absolute; left: 12px; top: 52px; font-size: 6px; line-height: 9px; color: var(--ink); }
  .card-front .person strong { font-weight: 600; }
  .card-front .contact { position: absolute; left: 92px; top: 48px; font-size: 5px; line-height: 8px; color: var(--grey); white-space: nowrap; }

  .card-back { left: 43px; top: 761px; width: 180px; height: 109px; background: #3d3f55; }
  .card-back .ghost { position: absolute; left: 14px; top: 28px; display: flex; align-items: center; gap: 8px; }
  .card-back .ghost .mark { width: 36px; height: 36px; background: rgba(255,255,255,.12); }
  .card-back .ghost .name { font-size: 12px; color: rgba(255,255,255,.12); }
  .card-back .web { position: absolute; left: 14px; bottom: 10px; font-size: 5.5px; color: #c9cad2; letter-spacing: .03em; }

  /* envelopes */
  .envelope-front { left: 266px; top: 672px; width: 432px; height: 234px; }
  .envelope-front .brand { left: 22px; top: 22px; }
  .envelope-front .brand .mark { width: 18px; height: 18px; }
  .envelope-front .brand .name { font-size: 13px; }
  .envelope-front .address { position: absolute; left: 22px; top: 54px; font-size: 6px; color: var(--grey); white-space: nowrap; }

  .envelope-back { left: 738px; top: 672px; width: 427px; height: 234px; }
  .envelope-back .flap { position: absolute; left: 0; right: 0; top: 0; height: 52px; background: var(--navy); }
  .envelope-back .web { position: absolute; right: 26px; top: 20px; font-size: 8px; color: #fff; letter-spacing: .12em; }
</style>
</head>
<body>

<section class="piece letterhead">
  <svg class="edge" viewBox="0 0 388 551" preserveAspectRatio="none" aria-hidden="true">
    <path d="M350 0 L388 0 L388 190 Q378 80 350 0 Z" fill="var(--navy)"/>
    <path d="M340 0 Q372 80 385 200" fill="none" stroke="var(--rule)" stroke-width="1.2"/>
    <path d="M0 360 Q18 480 52 551 L0 551 Z" fill="var(--navy)"/>
    <path d="M4 350 Q26 480 64 551" fill="none" stroke="var(--rule)" stroke-width="1.2"/>
  </svg>
  <div class="brand"><span class="mark"></span><span class="name">Marcus Varek</span></div>
  <div class="contact">
    718 Birchwood Avenue, Suite 300<br>Houston, TX 77019<br>T 713.555.0142<br>F 713.555.0143<br>C 713.555.0199<br>Varek@BrightCounselGroup.net<br>BrightCounselGroup.net
  </div>
  <div class="ghost"><span class="mark"></span><span class="name">Marcus Varek</span></div>
</section>

<section class="piece folder">
  <svg class="edge" viewBox="0 0 459 579" preserveAspectRatio="none" aria-hidden="true">
    <path d="M395 0 L459 0 L459 215 Q440 85 395 0 Z" fill="var(--navy)"/>
    <path d="M382 0 Q432 85 454 225" fill="none" stroke="var(--rule)" stroke-width="1.3"/>
    <path d="M0 370 Q22 495 62 579 L0 579 Z" fill="var(--navy)"/>
    <path d="M4 360 Q30 495 75 579" fill="none" stroke="var(--rule)" stroke-width="1.3"/>
  </svg>
  <div class="lockup">
    <span class="mark"></span>
    <span class="office">The Law Office of</span>
    <span class="name">Marcus Varek</span>
    <span class="suffix">PLLC</span>
  </div>
</section>

<section class="piece card-front">
  <div class="brand"><span class="mark"></span><span class="name">Marcus Varek</span></div>
  <div class="person"><strong>Marcus Varek</strong><br>Attorney at Law</div>
  <div class="contact">T 713.555.0142<br>F 713.555.0143<br>Varek@BrightCounselGroup.net<br>718 Birchwood Avenue<br>Houston, TX 77019</div>
</section>

<section class="piece card-back">
  <div class="ghost"><span class="mark"></span><span class="name">Marcus Varek</span></div>
  <div class="web">www.BrightCounselGroup.net</div>
</section>

<section class="piece envelope-front">
  <svg class="edge" viewBox="0 0 432 234" preserveAspectRatio="none" aria-hidden="true">
    <path d="M404 0 L432 0 L432 234 L424 234 Q424 100 404 0 Z" fill="var(--navy)"/>
    <path d="M396 0 Q418 100 418 234" fill="none" stroke="var(--rule)" stroke-width="1"/>
  </svg>
  <div class="brand"><span class="mark"></span><span class="name">Marcus Varek</span></div>
  <div class="address">718 Birchwood Avenue, Suite 300 Houston, TX 77019</div>
</section>

<section class="piece envelope-back">
  <div class="flap"></div>
  <div class="web">www.BrightCounselGroup.net</div>
</section>

</body>
</html>
```